business card for larch cove dental arts
Larch Cove Dental Arts
Professional
Rowland K. Bevacquist DDS
4 Mossbank Ln
Larch Cove, NY 14093
larchcovedentalarts@mailvane.example
larchcovedentalarts.example
On the card either at the bottom or the top I would like it to say "Implants Family Dentistry Cosmetic Dentistry" to tell people what i offer, or as a motto
________ ______ has an appointment
___/___/___@ ___:___am/pm
Mon Tues Wed Thurs Fri Sat
Logo design
the white may be easier to work with for the card

```html
<!DOCTYPE html>
<html lang="en">
<head>
<meta charset="utf-8">
<title>Larch Cove Dental Arts – Business Card</title>
<link rel="stylesheet" href="https://fonts.googleapis.com/css2?family=EB+Garamond:ital,wght@0,400;0,500;1,400&family=Cinzel:wght@400&family=Open+Sans:ital,wght@0,400;0,600;1,400;1,600&display=swap">
<style>
  :root {
    --backdrop: #e9e6e1;
    --card: #ffffff;
    --ink: #2b2b2b;
    --name-ink: #7b7592;
    --muted: #666666;
    --accent-blue: #3b63a8;
    --band-green: #b9d79c;
    --band-edge: #7fa85c;
    --band-ink: #2e5220;
    --rule: #9a9a9a;
    --mark-tint: #efefef;
  }
  * { box-sizing: border-box; margin: 0; padding: 0; }
  html, body { width: 1200px; height: 528px; overflow: hidden; }
  body { background: var(--backdrop); position: relative; font-family: "EB Garamond", serif; color: var(--ink); }

  .card {
    position: absolute; width: 526px; height: 298px;
    background: var(--card); border-radius: 12px; overflow: hidden;
    box-shadow: 0 6px 18px rgba(0,0,0,.25);
  }
  .card--front { left: 48px; top: 163px; }
  .card--back { left: 628px; top: 67px; }

  /* front */
  .brand { position: absolute; left: 22px; top: 36px; width: 220px; text-align: center; }
  .brand__dot { width: 78px; height: 78px; border-radius: 50%; background: var(--accent-blue); margin: 0 auto 36px; }
  .brand__name { font-size: 24px; line-height: 28px; color: var(--ink); text-transform: uppercase; letter-spacing: .5px; }
  .dentist { position: absolute; left: 300px; top: 113px; font-size: 18px; color: var(--name-ink); white-space: nowrap; }
  .contact { position: absolute; left: 300px; top: 156px; list-style: none; font-family: "Open Sans", sans-serif; font-size: 10.5px; color: var(--muted); }
  .contact li { display: flex; align-items: center; gap: 7px; height: 21px; white-space: nowrap; }
  .contact svg { width: 9px; height: 9px; fill: var(--muted); flex: none; }
  .front-rule { position: absolute; left: 0; right: 0; bottom: 40px; border-top: 1px solid #d6d6d6; }
  .band { position: absolute; left: 0; right: 0; bottom: 0; background: var(--band-green); border-top: 3px solid var(--band-edge); }
  .band--address { height: 34px; display: flex; align-items: center; justify-content: center; font-size: 14px; color: var(--ink); }

  /* back */
  .faint-mark { position: absolute; right: 22px; top: 10px; width: 128px; height: 150px; border-radius: 50%; background: var(--mark-tint); }
  .appt-title { position: absolute; left: 26px; top: 24px; font-family: "Cinzel", serif; font-weight: 400; font-size: 20px; letter-spacing: 1px; }
  .field { position: absolute; left: 26px; font-family: "Open Sans", sans-serif; font-size: 12px; color: var(--ink); display: flex; align-items: flex-end; gap: 6px; white-space: nowrap; }
  .field__line { display: inline-block; border-bottom: 1px dotted var(--rule); height: 12px; }
  .field__box { display: inline-block; width: 62px; height: 16px; border: 1px solid var(--ink); }
  .field--name { top: 84px; }
  .field--date { top: 120px; }
  .field--next { top: 160px; align-items: center; }
  .days { position: absolute; left: 26px; top: 198px; display: flex; gap: 9px; font-family: "Open Sans", sans-serif; font-weight: 600; font-size: 12px; color: var(--accent-blue); }
  .days span { display: flex; align-items: center; gap: 5px; }
  .days i { display: inline-block; width: 28px; height: 15px; border: 1px solid var(--ink); }
  .notice { position: absolute; left: 26px; top: 226px; font-family: "Open Sans", sans-serif; font-style: italic; font-size: 11.5px; color: var(--name-ink); }
  .band--motto { height: 36px; display: flex; align-items: center; padding-left: 26px; font-family: "Open Sans", sans-serif; font-style: italic; font-weight: 600; font-size: 12px; color: var(--band-ink); }
</style>
</head>
<body>
  <section class="card card--front" aria-label="Business card front">
    <div class="brand">
      <div class="brand__dot"></div>
      <div class="brand__name">Larch Cove<br>Dental Arts</div>
    </div>
    <p class="dentist">Rowland K. Bevacquist DDS</p>
    <ul class="contact">
      <li><svg viewBox="0 0 10 10"><path d="M2 0h2l1 3-1.5 1a6 6 0 0 0 2.5 2.5L7 5l3 1v2c0 1-1 2-2 2A8 8 0 0 1 0 2c0-1 1-2 2-2z"/></svg>845-555-0148</li>
      <li><svg viewBox="0 0 10 10"><rect x="0" y="2" width="10" height="6"/></svg>larchcovedentalarts@mailvane.example</li>
      <li><svg viewBox="0 0 10 10"><circle cx="5" cy="5" r="5"/></svg>larchcovedentalarts.example</li>
    </ul>
    <div class="front-rule"></div>
    <div class="band band--address">4 Mossbank Ln Larch Cove, NY 14093</div>
  </section>

  <section class="card card--back" aria-label="Business card back">
    <div class="faint-mark"></div>
    <h1 class="appt-title">YOUR APPOINTMENT</h1>
    <div class="field field--name">Name :<span class="field__line" style="width:270px"></span></div>
    <div class="field field--date">Date :<span class="field__line" style="width:120px"></span>Time :<span class="field__line" style="width:110px"></span>am / pm</div>
    <div class="field field--next">Next Appointment<span class="field__box" style="margin-left:20px"></span><span class="field__box" style="margin-left:14px"></span></div>
    <div class="days">
      <span>MON<i></i></span><span>TUE<i></i></span><span>WED<i></i></span><span>THU<i></i></span><span>FRI<i></i></span><span>SAT<i></i></span>
    </div>
    <p class="notice">We appreciate a 24 hr. notice for cancellations</p>
    <div class="band band--motto">Implants Family Dentistry, Cosmetic Dentistry</div>
  </section>
</body>
</html>
```